Geschäftspapier-Design für Anbieter einer Online-Ausbildung für den qualifizierten Krankentransport und Rettungsdienst
Zielgruppe
LOTH Online-Ausbildung für den qualifizierten Krankentransport und Rettungsdienst
Der qualifizierte Krankentransport und Rettungsdienst ist zuständig für den Transport- und die Versorgung von kranken und verletzten Menschen. LOTH Medizinische Ausbildung und Seminare hat sich als Privatschule für die präklinische Notfallmedizin auf Aus- und Weiterbildungen im E-Learning-Modul für diese zwei Fachbereiche spezialisiert. Alle unsere Fachausbildungen sind online in unserem modernen Campus mit überregionalem Zugang absolvierbar.
Aufgabenstellung
Wir benötigen eine Word-Briefvorlage für den alltäglichen Geschäftsverkehr in drei Ausführungen.
- Briefvorlage mit Angabe der Abteilung -> Sekretariat
- Briefvorlage mit Angabe der Abteilung -> Schulleitung
- Briefvorlage mit Angabe der Abteilung -> Geschäftsführung
- Briefvorlage mit Angabe der Abteilung -> Buchhaltung/ Forderungsmanagement
Die Vorlage sollte bitte folgende Angaben aufweisen:
LOTH Bildungsgesellschaft UG (haftungsbeschränkt)
Privatschule für prähospitale Rettungsmedizin
Standort unserer Verwaltung:
Farnhügel 7
15537 Erkner
Standort unseres Schulsitzes:
Am Quendelhof 48
D- 15537 Gosen- Neu Zittau
Schulleitung: Jutta Wildgrube & Matthias Lot
Ärztliche Leitung: Dr. Med. Ortwin Brasch
Pädagogische Leitung: Matthias Loth
Fachlicher Beirat: Dr. rer. med. Fabian Oswalt
Tel: 030 6270384 50
Fax: 030 6270384 51
E-Mail: info@loth-lehrwerkstatt.de
Web: www.loth-lehrwerkstatt.de
Vertreten durch: Jutta Wildgrube
Registereintrag: Eintragung im Handelsregister Registergericht: Amtsgericht Frankfurt (Oder) Registernummer: HRB 27403 FF

```html
<!DOCTYPE html>
<html lang="de">
<head>
<meta charset="utf-8">
<title>LOTH Bildungsgesellschaft – Briefvorlage Buchhaltung</title>
<link rel="stylesheet" href="https://fonts.googleapis.com/css2?family=Carlito:wght@400;700&display=swap">
<style>
  :root {
    --ink: #000000;
    --link: #1a0dab;
    --paper: #ffffff;
    --rule: #000000;
  }
  html, body {
    margin: 0;
    padding: 0;
    overflow: hidden;
    background: var(--paper);
  }
  .letterhead {
    position: relative;
    width: 848px;
    height: 1200px;
    overflow: hidden;
    background: var(--paper);
    color: var(--ink);
    font-family: "Carlito", "Calibri", sans-serif;
  }
  .brand-name {
    position: absolute;
    left: 560px;
    top: 66px;
    font-size: 30px;
    font-weight: 700;
    line-height: 1;
    color: var(--ink);
  }
  .sender-line {
    position: absolute;
    left: 101px;
    top: 121px;
    font-size: 11.5px;
    text-decoration: underline;
  }
  .board {
    position: absolute;
    left: 614px;
    top: 154px;
    width: 180px;
    margin: 0;
    font-size: 14.5px;
    line-height: 19.2px;
  }
  .board dt { font-weight: 700; margin: 0; }
  .board dd { margin: 0; }
  .department {
    position: absolute;
    left: 274px;
    top: 365px;
    font-size: 14.5px;
    line-height: 19.2px;
  }
  .department-label { font-weight: 700; }
  .footer-rule {
    position: absolute;
    left: 80px;
    top: 1019px;
    width: 722px;
    height: 0;
    border-top: 1px solid var(--rule);
  }
  .footer-col {
    position: absolute;
    top: 1030px;
    font-size: 11.5px;
    line-height: 15.8px;
  }
  .footer-col p { margin: 0 0 10.5px 0; }
  .footer-left { left: 88px; }
  .footer-right { left: 513px; }
  .footer-right a { color: var(--link); text-decoration: underline; }
</style>
</head>
<body>
<div class="letterhead">
  <div class="brand-name">LOTH</div>

  <div class="sender-line">LOTH Bildungsgesellschaft UG (haftungsbeschränkt)</div>

  <dl class="board">
    <dt>Schulleitung:</dt>
    <dd>Jutta Wildgrube &amp;<br>Matthias Lot</dd>
    <dt>Ärztliche Leitung:</dt>
    <dd>Dr. Med. Ortwin Brasch</dd>
    <dt>Pädagogische Leitung:</dt>
    <dd>Matthias Loth</dd>
    <dt>Fachlicher Beirat:</dt>
    <dd>Dr. rer. med. Fabian<br>Oswalt</dd>
  </dl>

  <div class="department">
    <div class="department-label">Abteilung:</div>
    <div>Buchhaltung/Forderungsmanagement</div>
  </div>

  <div class="footer-rule"></div>

  <div class="footer-col footer-left">
    <p>LOTH Bildungsgesellschaft UG (haftungsbeschränkt)<br>Privatschule für prähospitale Rettungsmedizin</p>
    <p>Standort unserer Verwaltung:<br>Farnhügel 7<br>D-15537 Erkner</p>
    <p>Standort unseres Schulsitzes:<br>Am Quendelhof 48<br>D-15537 Gosen- Neu Zittau</p>
  </div>

  <div class="footer-col footer-right">
    <p>Tel: 030 6270384 50<br>Fax: 030 6270384 51</p>
    <p>E-Mail: info@loth-lehrwerkstatt.de<br>Web: <a href="#">www.loth-lehrwerkstatt.de</a></p>
    <p>Handelsregister: Amtsgericht Frankfurt (Oder)</p>
    <p>Registriernummer: HRB 27403 FF</p>
  </div>
</div>
</body>
</html>
```